Guarenteed! - Homepage Website Design - Coding not required- Winner to complete further pages

Hi all,

We're looking at redesigning our current website with a few adjustments to other pages but the main adjustments will be on the homepage which is what this design request is for. Please note : any of these ideas can be changed if you have something particularly different / special in mind etc.

P.S Coding is not required, just a design.

- Our website -

Our website is simply a price comparison website that allows customers to find companies within their area at the best price. The products available are mostly related to the vehicle trade and all refer to vinyl. This includes the likes of vehicle window tint, vehicle colour change vehicle wrap, vehicle signage as well as other cosmetic vinyl modifications. We allow the customer to search for their product within their chosen area and receive a list of companies who supply their product within that area. From here they can compare prices and view further details on the company.

- What we're looking to do -

We're looking first of all to adjust how the website homepage is displayed, this includes adding images and adjusting the colours that are explained below:

First of all, we look to spread out each of the 12 products (which can be seen on the website as it stands) and add an image to each of the products (all being spaced out as shown in our sketch)

We've been told the website looks too busy so we're thinking if we adjust the colours to more simplier neutral colours as well as the main focus of the website being on the 12 images, that would be great.

- Logo + Banner -

Logo to remain top left although banner may be removed / adjusted to make simplier.

- Colours -

Adjustments - Colours shades
We want the website to still look exciting but simplify the colours. Needs to be kept up to date with the colours / textures etc (bright colours to highlight keypoints)
We're still looking to use either blue or orange or maybe both to highlight these keypoints but the main website to be light colours and maybe even black on white background. The entire homepage can be adjusted colour wise if you feel it fits into your theme including menu bars, banners etc. The key is to get this right with being not too overpowering with the colours but still look interesting and up to date.

- 1 - 4 steps banner - (text may change)

This sits just under the logo and explains to the user how easy the website is to use and the steps they need to take. This may change to a 1 - 5 steps but we're looking to have this designed once the overall colours / theme of the website is sorted.

- 12 images - 4 x 3

This is the main focus of the website and will be the main focus of what the customer sees first of all. This will be where they select their product and then underneath, enter their postcode and distance they would like to search within. As explained further up, we have some of the product images available so if you can where possible add these to the design and then duplicate the images on those we currently don't have available.

- 12 Images -Titles -

These titles will be in this order from left to right and etc

- Colour Change Wrap
- Printed Vehicle Wrap
- Window Tint
- Headlight Tint
- Vehicle Signage
- Shop Signage
- Roof Vinyl Wrap
- Bonnet Vinyl Wrap
- Carbon Fibre Vinyl
- Stickerbomb Vinyl
- Clear Protective Vinyl
- Wheel Refurb

Text to be quite large, centered and with the o to the left of the title. Short titles like 'Window Tint' should fit on one line in the middle of the box where as titles such as ' Stickerbomb Vinyl Wrap' should have the 'Stickerbomb Vinyl' on the first line with the 'Wrap' on the line below. The background of this text is up to experient, might be worth just a simple colour or it might be worth using a bright blue or orange to keep in with the theme of the logo etc.

These will also have the circle tick box to the left of the title (as on the current website) where the customer clicks to select the product they have available.
We were also thinking that if when the customer ticks the circle on their selected box, the box is highlighted in some way to show this.

- Search Block -

This will appear under the 12 images and allows the customer to input their postcode and distance for the search criteria. Colours on this can of course be adjusted to keep in theme with the website.

- Under the 12 Images -

- Block underneath the 12 images and search block -

To the left will be some key bullet points about the website - maybe 4 or 5 with a green tick to the left of this. Background colour will probably be best to be a light colour, possibly grey.

Then to the right of this will appear 4 images, 2 before and 2 after when applying these products. Images to be used aren't fully decided on and we would like this stage of the design left to the end when the rest of the theme etc have been decided on.

Attached images are as follows :
- How the website looks as it stands
- The fold line on the website (obviously important)
- Our rough sketch of how we'd like the website homepage to look.
- We have 7 of the images ready that are all attached in this one file. Please duplicate the images on those that currently don't have the image available.

We will also be requesting a website developer to put this into action if our current designer falls through so please feel free to contact us if potentially interested.

The layout can change if you can think of something particular different / unique that works with this design. The main idea is to not only get the 12 products on view to the viewers but also the keypoints and before and after images.

Any questions, please ask away as we're bound to have forgotten a few things.

Thanks and good luck!

Hi all, keep the designs coming.

We haven't quite seen that extra special design we're after. As stated, we're after something fairly simple to suit the youth as well as the middle aged but we're also after something that bit special.

Colours to concentrate on are still and orange etc although feel free to use other colours if you have anything special in mind.

Please experience and we'll give you our honest feedback.

Many thanks all and good luck!

Hi all, this is a message to all the designers.

Some good designs coming in but we're still after that something special for the website design. Keep the designs coming and please feel free to experiment with the design colours, layout etc.

The basic principle of the website needs to remain regarding the 12 products, search within block and 4 steps all appearing on the homepage.

The 4 steps seems to work best when it's got text as well as some simple images next to this.

A variation with the product titles with how to display this, some designers have gone with a simple white background whereas others have gone with colours. Please experiment here and where possible, add a contract / texture to the colour. Please remember the product titles needs to be clear, centured and with the circle tick box to the left of it. 

We're after a fairly simple design although we need it to look 21st century, up to date as well as interesting. The key points straight away are the 4 steps as well as the 12 products so try to guide the viewer to these areas a little.

White background behind the 12 images seems to be a much, although a light colour could possibly work.

The keypoints underneath these 12 products are too very important as it outlines what we do etc. Tick colour can vary.

Next to these keypoints will be the 'before' and 'after' images, these images needs to be fairly small and ensure there is white background around the image itself.

Good luck all and any questions, feel free to ask away.

Thanks!

Hi,

 Thank you for your time and effort with these designs, we are very nearly there with the design but we've thought of something that may work for the homepage. A curved arrow from step 1 pointing to the products, this may or may not work but feel free to give it a go.

Many thanks,

Thank you to everyone for your time and efforts with the design. It's hugely appreciated so thank you all once again.

Wish you all the luck in the future.

```html
<!DOCTYPE html>
<html lang="en">
<head>
<meta charset="utf-8">
<title>Wrap Locator – Find a Professional Vinyl Installer</title>
<link href="https://fonts.googleapis.com/css2?family=Open+Sans:wght@300;400;600;700&display=swap" rel="stylesheet">
<style>
  :root {
    --orange: #f7941d;
    --ink: #222222;
    --text: #333333;
    --muted: #555555;
    --line: #a8a8a8;
    --white: #ffffff;
    --dark: #3d3d3d;
    --brand: #3c4f8f;
    --social: #4a6aa8;
    --social-alt: #2aa9dd;
  }
  * { box-sizing: border-box; margin: 0; padding: 0; }
  html, body { width: 1200px; height: 628px; overflow: hidden; }
  body {
    position: relative;
    background: var(--white);
    font-family: "Open Sans", Arial, sans-serif;
    color: var(--text);
  }

  /* Header */
  .site-header { position: absolute; left: 0; top: 0; width: 1200px; height: 93px; border-bottom: 5px solid var(--orange); }
  .brand { position: absolute; left: 150px; top: 14px; display: flex; align-items: center; gap: 10px; }
  .brand-mark { width: 44px; height: 44px; border-radius: 50%; background: var(--orange); }
  .brand-name { font-size: 30px; font-weight: 700; color: var(--brand); letter-spacing: 0.5px; line-height: 1; }
  .brand-tagline { position: absolute; left: 150px; top: 64px; font-size: 11px; font-weight: 600; color: var(--muted); }

  .social { position: absolute; top: 10px; width: 92px; height: 33px; display: flex; align-items: center; gap: 5px; padding: 0 5px; border: 2px solid var(--social); border-radius: 5px; color: var(--social); text-decoration: none; white-space: nowrap; overflow: hidden; }
  .social-like { left: 853px; }
  .social-follow { left: 951px; border-color: #3cc0ef; color: var(--social-alt); }
  .social-dot { width: 10px; height: 10px; background: currentColor; border-radius: 2px; flex: none; }
  .social-text { display: flex; flex-direction: column; line-height: 1.05; }
  .social-small { font-size: 9px; font-weight: 600; }
  .social-name { font-size: 11px; font-weight: 700; }

  .main-nav { position: absolute; left: 0; top: 53px; width: 1200px; height: 35px; }
  .main-nav a { position: absolute; top: 0; height: 35px; line-height: 35px; font-size: 15px; color: var(--ink); text-decoration: none; white-space: nowrap; }
  .main-nav a.is-active { left: 488px; width: 72px; text-align: center; background: var(--orange); color: var(--white); }
  .nav-about { left: 584px; }
  .nav-contact { left: 672px; }
  .nav-blog { left: 773px; }
  .nav-list { left: 856px; }

  /* Hero */
  .hero { position: absolute; left: 0; top: 93px; width: 1200px; height: 167px; background: linear-gradient(90deg, #3a3a3a, #555555 50%, #3f3f3f); border-bottom: 5px solid var(--orange); }
  .hero-visual { position: absolute; left: 196px; top: 10px; width: 262px; height: 146px; border-radius: 22px 40px 14px 14px; background: linear-gradient(180deg, #8fb6e0 0%, #e9eef2 45%, #5f9a2a 100%); }
  .hero-copy { position: absolute; left: 526px; top: 34px; color: var(--white); }
  .hero-line { font-size: 27px; font-weight: 300; line-height: 1.2; }
  .hero-title { font-size: 34px; font-weight: 700; line-height: 1.1; margin: 2px 0 3px; }
  .hero-title span { color: var(--orange); }
  .hero-arrow { position: absolute; top: 66px; }
  .hero-arrow.prev { left: 40px; }
  .hero-arrow.next { left: 1134px; }

  /* Steps */
  .steps-title { position: absolute; left: 0; top: 268px; width: 1200px; text-align: center; font-size: 24px; font-weight: 600; color: var(--ink); }
  .steps { position: absolute; left: 157px; top: 311px; display: flex; gap: 21px; }
  .step { position: relative; width: 206px; height: 102px; border: 1px solid var(--line); background: var(--white); text-align: center; }
  .step-corner { position: absolute; left: 0; top: 0; width: 42px; height: 42px; background: var(--orange); clip-path: polygon(0 0, 100% 0, 0 100%); }
  .step-number { position: absolute; left: 6px; top: 2px; font-size: 15px; font-weight: 700; color: var(--white); }
  .step-icon { display: block; margin: 13px auto 0; }
  .step-text { font-size: 14px; line-height: 1.2; color: var(--ink); margin-top: 4px; }

  /* Products */
  .products { position: absolute; left: 0; top: 431px; width: 1200px; height: 197px; background: var(--dark); }
  .products-title { position: absolute; left: 157px; top: 16px; font-size: 20px; font-weight: 400; color: var(--white); }
  .product-grid { position: absolute; left: 157px; top: 52px; display: flex; gap: 20px; }
  .product { width: 206px; height: 136px; background: var(--white); position: relative; }
  .product-image { position: absolute; left: 50%; top: 6px; transform: translateX(-50%); width: 120px; height: 76px; border-radius: 18px 26px 10px 10px; }
  .product-label { position: absolute; left: 0; width: 100%; display: flex; justify-content: center; align-items: center; gap: 9px; font-size: 17px; color: var(--muted); line-height: 1.05; text-align: center; }
  .radio { width: 14px; height: 14px; border: 2px solid var(--orange); border-radius: 50%; flex: none; }
  .img-red { background: linear-gradient(160deg, #e33a2c, #9e1b12); }
  .img-van { background: linear-gradient(180deg, #9ec2e6, #eef1f3 50%, #5e9a2b); width: 140px; }
  .img-silver { background: linear-gradient(160deg, #e6e6e6, #9c9c9c); width: 170px; height: 74px; }
  .img-navy { background: linear-gradient(160deg, #3a4a7a, #111a33); width: 118px; height: 92px; }
</style>
</head>
<body>

<header class="site-header">
  <div class="brand">
    <span class="brand-mark"></span>
    <span class="brand-name">WRAP LOCATOR</span>
  </div>
  <div class="brand-tagline">Find and Compare Vinyl Installers</div>

  <a class="social social-like" href="#"><span class="social-dot"></span><span class="social-text"><span class="social-small">Like us on</span><span class="social-name">Friendbook</span></span></a>
  <a class="social social-follow" href="#"><span class="social-dot"></span><span class="social-text"><span class="social-small">follow us on</span><span class="social-name">Chirper</span></span></a>

  <nav class="main-nav">
    <a class="is-active" href="#">HOME</a>
    <a class="nav-about" href="#">ABOUT</a>
    <a class="nav-contact" href="#">CONTACT</a>
    <a class="nav-blog" href="#">BLOG</a>
    <a class="nav-list" href="#">LIST YOUR COMPANY HERE</a>
  </nav>
</header>

<section class="hero">
  <div class="hero-visual" role="img" aria-label="Side view of a van with a printed green and sky vinyl wrap"></div>
  <div class="hero-copy">
    <div class="hero-line">FIND A PROFESSIONAL</div>
    <div class="hero-title"><span>VINYL INSTALLER</span> TODAY</div>
    <div class="hero-line">SEARCH &amp; SAVE IN SECONDS</div>
  </div>
  <svg class="hero-arrow prev" width="24" height="34" viewBox="0 0 24 34"><path d="M18 3 L5 17 L18 31" fill="none" stroke="#fff" stroke-width="2.5"/></svg>
  <svg class="hero-arrow next" width="24" height="34" viewBox="0 0 24 34"><path d="M6 3 L19 17 L6 31" fill="none" stroke="#fff" stroke-width="2.5"/></svg>
</section>

<h2 class="steps-title">4 Easy Steps to get Started</h2>
<div class="steps">
  <div class="step">
    <div class="step-corner"></div><span class="step-number">1</span>
    <svg class="step-icon" width="36" height="36" viewBox="0 0 36 36">
      <rect x="4" y="8" width="24" height="24" fill="none" stroke="#f7941d" stroke-width="3"/>
      <path d="M10 18 L16 25 L33 4" fill="none" stroke="#f7941d" stroke-width="4"/>
    </svg>
    <div class="step-text">Select Chosen<br>Product</div>
  </div>
  <div class="step">
    <div class="step-corner"></div><span class="step-number">2</span>
    <svg class="step-icon" width="36" height="36" viewBox="0 0 36 36">
      <rect x="14" y="2" width="8" height="32" fill="#f7941d" transform="rotate(45 18 18)"/>
      <rect x="14" y="2" width="8" height="32" fill="#f7941d" transform="rotate(-45 18 18)"/>
    </svg>
    <div class="step-text">Input Postcode, Distance<br>+ search</div>
  </div>
  <div class="step">
    <div class="step-corner"></div><span class="step-number">3</span>
    <svg class="step-icon" width="36" height="36" viewBox="0 0 36 36">
      <path d="M4 4 H17 L32 19 L19 32 L4 17 Z" fill="#f7941d"/>
      <circle cx="10" cy="10" r="2.5" fill="#fff"/>
    </svg>
    <div class="step-text">Compare companies<br>+ prices</div>
  </div>
  <div class="step">
    <div class="step-corner"></div><span class="step-number">4</span>
    <svg class="step-icon" width="36" height="36" viewBox="0 0 36 36">
      <circle cx="18" cy="11" r="8" fill="#f7941d"/>
      <path d="M3 34 C4 22 32 22 33 34 Z" fill="#f7941d"/>
    </svg>
    <div class="step-text">Contact chosen<br>company</div>
  </div>
</div>

<section class="products">
  <h3 class="products-title">Select Chosen Product:</h3>
  <div class="product-grid">
    <div class="product">
      <div class="product-image img-red" role="img" aria-label="Red car with a colour change wrap"></div>
      <div class="product-label" style="top:92px"><span class="radio"></span><span>Color Change<br>Wrap</span></div>
    </div>
    <div class="product">
      <div class="product-image img-van" role="img" aria-label="Van with a printed vehicle wrap"></div>
      <div class="product-label" style="top:94px"><span class="radio"></span><span>Printed Vehicle<br>Wrap</span></div>
    </div>
    <div class="product">
      <div class="product-image img-silver" role="img" aria-label="Silver sports car with tinted windows"></div>
      <div class="product-label" style="top:102px"><span class="radio"></span><span>Window Tint</span></div>
    </div>
    <div class="product">
      <div class="product-image img-navy" role="img" aria-label="Dark blue car with tinted headlights"></div>
      <div class="product-label" style="top:101px"><span class="radio"></span><span>Headlight Tint</span></div>
    </div>
  </div>
</section>

</body>
</html>
```